Two flyers with cover pages for business services company

We need to create two double sided A4 flyers for our company. We are a company that provides professional services for businesses in Dubai, UAE.
Please note that there are two different flyers. The design must be identical. Each has a cover page. The cover page will be duplicated for both flyers.
Please note that we have added images of the Dubai skyline, clip art as place-hold/temporary images. These can be changed to be more fitting to your design. We prefer to have free images where possible but are open to purchasing Pixelorra images if required.
We have recommended a colour palet below. You are welcome to change some colours to be more fitting to the design. However, we must have black, white and blue and per the logo.
Target Market(s)
Businesses, entrepreneurs, professionals
Industry/Entity Type
Business Service
Requirements
Must have
- The cover page should be less crowded and more visual. So mostly images with our logo and tagline.

```html
<!DOCTYPE html>
<html lang="en">
<head>
<meta charset="utf-8">
<title>Novaro – Business Sponsorship Flyers</title>
<link rel="stylesheet" href="https://fonts.googleapis.com/css2?family=Roboto+Condensed:wght@300;400;700&display=swap">
<style>
  :root{
    --page:#e8e8e8;
    --white:#ffffff;
    --ink:#1c1c1c;
    --grey:#3a3a3a;
    --blue:#2f6db2;
    --navy:#1b55a3;
    --orange:#f18a1f;
    --photo-light:#f4eeeb;
    --photo-warm:#e6d2c8;
    --photo-cool:#e3e6ea;
  }
  *{box-sizing:border-box;margin:0;padding:0}
  html,body{width:1200px;height:1200px;overflow:hidden;background:var(--page)}
  body{position:relative;font-family:"Roboto Condensed",sans-serif;color:var(--ink)}

  .flyer{position:absolute;top:179px;width:560px;height:791px;background:var(--white);overflow:hidden;box-shadow:0 2px 6px rgba(0,0,0,.15)}
  .flyer--cover{left:30px}
  .flyer--offer{left:614px}

  /* cover */
  .cover-photo{position:absolute;inset:0;
    background:linear-gradient(165deg,var(--photo-light) 0%,#faf7f6 40%,var(--photo-warm) 78%,#d9cfca 100%)}
  .cover-fade{position:absolute;inset:0;background:linear-gradient(90deg,rgba(255,255,255,0) 40%,rgba(255,255,255,.75) 70%,rgba(255,255,255,0) 100%)}
  .cover-headline{position:absolute;left:278px;top:36px;font-weight:700;font-size:41px;line-height:43px;letter-spacing:-.5px;color:var(--ink)}
  .badge{position:absolute;border-radius:50%;background:var(--blue);border:5px solid var(--orange);color:var(--white);display:flex;flex-direction:column;align-items:center;justify-content:center;text-align:center;font-weight:300;text-transform:uppercase;white-space:nowrap}
  .badge b{font-weight:700}
  .badge--sponsor{left:278px;top:213px;width:152px;height:152px;font-size:21px;line-height:23px;letter-spacing:-.6px}
  .brand{position:absolute;left:24px;top:700px;display:flex;align-items:center;gap:12px}
  .brand-dot{width:38px;height:38px;border-radius:50%;background:var(--blue)}
  .brand-name{font-size:38px;font-weight:400;color:var(--grey)}
  .cover-web{position:absolute;left:376px;top:712px;font-size:21px;letter-spacing:1px;color:var(--ink)}

  /* offer page */
  .offer-title{position:absolute;left:0;right:0;top:16px;text-align:center;font-weight:300;font-size:36px;line-height:40px;color:var(--navy)}
  .offer-title span{display:block}
  .team-photo{position:absolute;left:0;top:99px;width:560px;height:258px;
    background:linear-gradient(180deg,var(--photo-cool) 0%,#d8dbe0 100%)}
  .badge--install,.badge--guarantee{left:32px;width:140px;height:140px;font-size:16px;line-height:16px;letter-spacing:-.6px}
  .badge--install{top:341px}
  .badge--guarantee{top:496px}
  .offer-body{position:absolute;left:183px;top:374px;width:370px}
  .offer-sub{font-size:16.5px;font-weight:400;color:var(--navy);margin-bottom:6px}
  .offer-text{font-size:13.5px;font-weight:300;line-height:20px;margin-bottom:10px}
  .offer-text b{font-weight:400}
  .offer-list{list-style:none;font-size:12.5px;font-weight:300;line-height:18.6px}
  .offer-list li::before{content:"- "}
  .offer-list b{font-weight:700}
  .cta{position:absolute;left:21px;top:674px;font-size:14px;font-weight:300;text-transform:uppercase}
  .cta b{font-weight:700}
  .phone{position:absolute;left:21px;top:688px;font-size:34px;font-weight:400;color:var(--orange)}
  .contact{position:absolute;top:738px;display:flex;align-items:center;gap:6px;font-size:11.5px;font-weight:300;line-height:13px}
  .contact--address{left:21px}
  .contact--web{left:193px}
  .portrait{position:absolute;left:322px;top:658px;width:112px;height:112px;border-radius:50%;border:3px solid var(--orange);background:linear-gradient(180deg,#e4e6e9,#c9ccd1);z-index:2}
  .name-tag{position:absolute;left:424px;top:686px;width:112px;height:62px;background:var(--orange);color:var(--white);padding:12px 0 0 14px;font-size:15px;line-height:18px}
  .name-tag em{display:block;font-size:12px;font-weight:700}
</style>
</head>
<body>

<section class="flyer flyer--cover">
  <div class="cover-photo" role="img" aria-label="Soft-focus photo of a businessman behind two hands in a firm handshake"></div>
  <div class="cover-fade"></div>
  <h1 class="cover-headline">Are you getting<br>REAL value<br>from your<br>current sponsor?</h1>
  <div class="badge badge--sponsor"><b>50% OFF</b>Your current<br>sponsorship</div>
  <div class="brand"><span class="brand-dot"></span><span class="brand-name">Novaro</span></div>
  <div class="cover-web">www.novaro.ae</div>
</section>

<section class="flyer flyer--offer">
  <h2 class="offer-title"><span>DO YOU NEED HELP TO INCREASE</span><span>YOUR SALES?</span></h2>
  <div class="team-photo" role="img" aria-label="Photo of three businessmen reviewing documents together at an office desk"></div>
  <div class="badge badge--install">As low as<br><span><b>1,500 AED</b> easy</span>monthly<br>installments</div>
  <div class="badge badge--guarantee"><b>Satisfaction<br>guaranteed</b>100%<br>or your<br>money back</div>

  <div class="offer-body">
    <h3 class="offer-sub">Grow Your Business Through Our Extensive Network</h3>
    <p class="offer-text">Use our <b>3,000+ Business Connections,<br>570+Decision Makers,</b> MDs, CEOs, Heads of Purchasing</p>
    <h3 class="offer-sub">The Best Offer in the Market</h3>
    <ul class="offer-list">
      <li><b>50% off</b> your current sponsorship fees</li>
      <li><b>Free sponsorship</b> for 12 months</li>
      <li>Low monthly installments (starting at&nbsp; AED 1,500)</li>
      <li>We can be active or silent sponsors</li>
      <li>Unique legal structure which allows you to exit any time</li>
      <li>Help you increase your sales</li>
      <li>VIP introductions and connections</li>
      <li>Legal and mediation support</li>
      <li>We have been in this market since 2004</li>
    </ul>
  </div>

  <p class="cta">Call us now for a <b>free consultation</b> on</p>
  <p class="phone">04 555 0182</p>
  <div class="contact contact--address">
    <svg width="18" height="24" viewBox="0 0 18 24"><path d="M9 1.5a7 7 0 0 0-7 7c0 5 7 13.5 7 13.5s7-8.5 7-13.5a7 7 0 0 0-7-7z" fill="none" stroke="#1c1c1c" stroke-width="1.8"/><circle cx="9" cy="8.5" r="2.4" fill="#1c1c1c"/></svg>
    <span>Crescent Business Tower,<br>24th Floor Dubai, UAE</span>
  </div>
  <div class="contact contact--web">
    <svg width="22" height="22" viewBox="0 0 22 22" fill="none" stroke="#1c1c1c" stroke-width="1.3"><circle cx="11" cy="11" r="9.5"/><ellipse cx="11" cy="11" rx="4.2" ry="9.5"/><path d="M1.5 11h19M3 6h16M3 16h16"/></svg>
    <span>www.novaro.ae</span>
  </div>
  <div class="portrait" role="img" aria-label="Portrait photo of the managing director"></div>
  <div class="name-tag">Daniel Marsh,<em>Managing Director</em></div>
</section>

</body>
</html>
```